Webdesign Bestattungswesen Wiesentrup
Zielgruppe
Bestattungsunternehmen
Aufgabenstellung
- Seite soll keine Kopie der alten Webseite werden
- Logo muss unverändert bleiben
- KEIN schwarz als Hauptfarbe !
- sanfte Farben

```html
<!DOCTYPE html>
<html lang="de">
<head>
<meta charset="utf-8">
<title>Bestattungswesen Wiesentrup</title>
<link href="https://fonts.googleapis.com/css2?family=Gelasio:wght@400;700&family=Arimo:wght@400&family=Open+Sans:wght@400;600&display=swap" rel="stylesheet">
<style>
:root{
  --mauve:#b39b9c;
  --mauve-deep:#a88f90;
  --mauve-soft:#c9b7b8;
  --blush:#e4dadb;
  --gold:#c9955a;
  --white:#ffffff;
  --text:#333333;
  --serif:"Gelasio", Georgia, serif;
  --sans:"Arimo", Arial, sans-serif;
  --footer-sans:"Open Sans", Arial, sans-serif;
}
*{margin:0;padding:0;box-sizing:border-box}
html,body{width:1200px;height:3527px;overflow:hidden;background:var(--white)}
body{position:relative;font-family:var(--sans);color:var(--text)}
.abs{position:absolute}
section,header,footer{position:absolute;left:0;width:1200px}

.topbar{top:0;height:25px;background:var(--mauve);display:flex;justify-content:center;align-items:center;gap:14px}
.topbar svg{width:14px;height:14px}

.site-header{top:25px;height:59px;background:var(--white)}
.brand{left:178px;top:6px;width:230px;font-family:var(--serif);color:var(--gold)}
.brand-name{font-size:17px;font-weight:700;letter-spacing:.3px;white-space:nowrap}
.brand-owner{font-size:7.5px;text-align:right;margin-top:1px}
.brand-rule{height:1px;background:var(--gold);margin-top:4px}
.main-nav{left:575px;top:36px;display:flex;gap:7px;font-family:var(--serif);font-size:8.5px;color:#555;letter-spacing:.2px}

.hero{top:84px;height:446px;background:
  radial-gradient(circle at 12% 70%,#fff1e6 0,#f3d8cf 14%,transparent 28%),
  radial-gradient(circle at 90% 60%,#ffe8d2 0,#f1d3cb 18%,transparent 34%),
  radial-gradient(circle at 55% 20%,#f7e3dc 0,transparent 30%),
  radial-gradient(circle at 25% 95%,#f9c98a 0,transparent 12%),
  linear-gradient(160deg,#e6cdc7,#d7b6b2 50%,#e9cfc8);border-top:1px solid #e9d47a}
.hero-panel{left:0;top:141px;width:729px;height:202px;background:rgba(175,145,150,.45)}
.hero-rule{left:193px;top:186px;width:3px;height:93px;background:var(--gold)}
.hero-title{left:214px;top:179px;font-family:var(--serif);font-weight:400;font-size:33px;line-height:34px;color:var(--white);white-space:nowrap}
.hero-sub{left:214px;top:255px;font-family:var(--sans);font-size:21px;color:var(--white)}

.pill{position:absolute;display:flex;align-items:center;justify-content:center;border-radius:27px;font-family:var(--serif);font-weight:700;font-size:15px;letter-spacing:.5px;text-transform:uppercase}
.pill-light{background:var(--white);color:var(--mauve)}
.pill-gold{background:var(--white);color:var(--gold)}
.pill-solid{background:var(--mauve);color:var(--white)}
.phone-mark{position:absolute;width:40px;height:40px}

.services{top:530px;height:455px;background:var(--mauve-soft)}
.services-title{top:86px;width:100%;text-align:center;font-family:var(--serif);font-weight:700;font-size:23px;color:var(--white);letter-spacing:.5px}
.service-card{position:absolute;top:151px;width:266px;height:145px;background:var(--white);border:1px solid #d9b998;border-radius:3px;display:flex;flex-direction:column;align-items:center;justify-content:flex-end;padding-bottom:26px;gap:18px}
.service-card svg{width:60px;height:56px}
.service-card span{font-family:var(--serif);font-size:15px;color:var(--gold);letter-spacing:.3px}

.section-title{position:absolute;width:100%;text-align:center;font-family:var(--serif);font-weight:700;font-size:23px;color:var(--mauve);letter-spacing:.4px}
.ornament{position:absolute;left:518px;width:164px;height:50px;border-radius:50%;background:radial-gradient(ellipse,#e1d3d3 0,#efe6e6 55%,transparent 72%)}
.copy{position:absolute;font-size:10px;line-height:22.6px;color:var(--text)}
.copy p+p{margin-top:22.6px}

.about{top:985px;height:590px}
.reach{top:1575px;height:325px;background:var(--blush)}
.reach .copy{text-align:center}
.care{top:1900px;height:396px}

.gallery{top:2296px;height:510px}
.tile{position:absolute}
.tile-coffin{left:0;top:0;width:597px;height:255px;background:linear-gradient(100deg,#3a2f30 0,#6d5757 30%,#c9a9a6 55%,#efdede 70%,#8a5a44 88%,#5b3a2c)}
.tile-urn{left:597px;top:0;width:302px;height:255px;background:radial-gradient(circle at 50% 75%,#7c1f26 0,#4c4a30 25%,transparent 45%),linear-gradient(180deg,#2f3a2a,#b68a56 60%,#5c4836)}
.tile-mauve{left:899px;top:0;width:301px;height:255px;background:var(--mauve)}
.tile-cards{left:0;top:255px;width:296px;height:255px;background:linear-gradient(135deg,#d8c8c8,#c9b3b3 60%,#bfa8a9);display:flex;align-items:center;justify-content:center;text-align:center}
.tile-cards p{font-family:var(--serif);font-weight:700;font-size:10.5px;line-height:22.5px;color:var(--white);letter-spacing:.4px;width:250px}
.tile-mauve2{left:296px;top:255px;width:301px;height:255px;background:var(--mauve)}
.tile-water{left:597px;top:255px;width:603px;height:255px;background:radial-gradient(ellipse at 48% 55%,#b0254e 0,#5a4a3a 25%,transparent 45%),linear-gradient(180deg,#d99766 0,#c3827a 35%,#6e5d6d 70%,#4c5068)}

.region{top:2806px;height:393px}
.region .copy{text-align:center}

.site-footer{top:3199px;height:289px;background:var(--blush);font-family:var(--footer-sans)}
.foot-head{position:absolute;font-family:var(--serif);font-weight:400;font-size:15px;color:#333}
.foot-lines{position:absolute;font-size:10px;line-height:22.5px;color:#333}
.badge{position:absolute;top:97px;height:101px;background:#f4f0f0;border:1px solid #cfc5c5}
.bottombar{top:3488px;height:39px;background:var(--gold);display:flex;justify-content:center;align-items:center;gap:8px;font-family:var(--footer-sans);font-weight:600;font-size:8.5px;color:var(--white)}
</style>
</head>
<body>

<header class="topbar">
  <svg viewBox="0 0 16 16" aria-label="E-Mail"><rect x="1" y="3" width="14" height="10" fill="none" stroke="#fff" stroke-width="1.5"/><path d="M1 3l7 6 7-6" fill="none" stroke="#fff" stroke-width="1.5"/></svg>
  <svg viewBox="0 0 16 16" aria-label="Telefon"><path d="M4 1l3 3-2 2c1 2 3 4 5 5l2-2 3 3-2 3C7 14 2 9 1 3z" fill="#fff"/></svg>
  <svg viewBox="0 0 16 16" aria-label="Standort"><path d="M8 1a5 5 0 0 0-5 5c0 4 5 9 5 9s5-5 5-9a5 5 0 0 0-5-5z" fill="none" stroke="#fff" stroke-width="1.6"/><circle cx="8" cy="6" r="1.8" fill="#fff"/></svg>
</header>

<header class="site-header">
  <div class="brand abs">
    <div class="brand-name">Bestattungswesen Wiesentrup</div>
    <div class="brand-owner">Inh. Marlene Hoffmann</div>
    <div class="brand-rule"></div>
  </div>
  <nav class="main-nav abs">
    <span>HOME</span><span>ERDBESTATTUNGEN</span><span>FEUERBESTATTUNG</span><span>VORSORGE</span><span>BESTATTUNGSKOSTEN</span><span>RATGEBER/FAQ</span>
  </nav>
</header>

<section class="hero" role="img" aria-label="Foto: brennende weiße Kerzen in warmem Licht">
  <div class="hero-panel abs"></div>
  <div class="hero-rule abs"></div>
  <h1 class="hero-title abs">Beim &nbsp;Abschied an Ihrer Seite:<br>Bestattungswesen Wiesentrup</h1>
  <div class="hero-sub abs">empathisch · professionell</div>
</section>

<section class="services">
  <h2 class="services-title abs">VERTRAUENSVOLL VERABSCHIEDEN.</h2>
  <div class="service-card" style="left:177px">
    <svg viewBox="0 0 60 56" fill="none" stroke="#c9955a" stroke-width="2.2"><path d="M30 4v34M20 14h20"/><path d="M8 50c6-12 38-12 44 0z"/><path d="M4 52h52"/></svg>
    <span>ERDBESTATTUNGEN</span>
  </div>
  <div class="service-card" style="left:466px">
    <svg viewBox="0 0 60 56" fill="none" stroke="#c9955a" stroke-width="2.2"><rect x="23" y="3" width="14" height="6"/><path d="M21 10h18c6 6 8 14 5 24-2 7-4 12-4 12H20s-2-5-4-12c-3-10-1-18 5-24z"/><path d="M17 24h26M18 36h24M20 51h20"/></svg>
    <span>FEUERBESTATTUNGEN</span>
  </div>
  <div class="service-card" style="left:752px">
    <svg viewBox="0 0 60 56" fill="none" stroke="#c9955a" stroke-width="2.2"><path d="M30 48S10 36 10 22a10 10 0 0 1 20-4 10 10 0 0 1 20 4c0 14-20 26-20 26z"/></svg>
    <span>VORSORGE</span>
  </div>
  <div class="pill pill-light" style="left:493px;top:336px;width:221px;height:53px">BERATEN LASSEN</div>
</section>

<div class="pill pill-gold" style="left:493px;top:514px;width:221px;height:51px;z-index:2">SOFORTHILFE (24/7)</div>
<svg class="phone-mark" style="left:578px;top:488px;z-index:3" viewBox="0 0 40 40"><path d="M8 2l8 7-4 6c3 6 7 10 13 13l6-4 7 8-5 6C17 36 4 23 3 8z" fill="#c9955a"/></svg>

<section class="about">
  <div class="ornament" style="top:92px" role="img" aria-label="Zierelement: gekreuzte Palmzweige"></div>
  <h2 class="section-title" style="top:158px">BESTATTUNGSWESEN WIESENTRUP – WÜRDEVOLLE BESTATTUNGEN</h2>
  <div class="copy" style="left:187px;top:213px;width:395px">
    <p>Vieles bewegt Menschen, die nahe Verwandte oder gute Freunde verloren haben. Wie schwer ist es dann, einen klaren Gedanken zu fassen und notwendige Entscheidungen zu treffen. Wir möchten in diesen schweren Stunden für alle Betroffenen hilfreiche und verständnisvolle Begleiter sein. In dieser persönlich schwierigen Zeit ist es wichtig, einen vertrauenswürdigen und erfahrenen Partner zur Seite zu haben.</p>
    <p>Als fachgeprüfte Bestatter mit über 25-jähriger Berufserfahrung sind der Respekt des letzten Willens des Verstorbenen und die Wünsche der Angehörigen eine Selbstverständlichkeit.</p>
  </div>
  <div class="copy" style="left:619px;top:213px;width:395px">
    <p>Ob eine Bestattung in aller Stille im engsten Kreis der Familie, besondere Wünsche, eine Trauerfeier im großen Rahmen oder eine kirchliche Grablegungszeremonie – unser Team sorgt für einen würdigen Rahmen mit allen Details und kümmert sich sorgfältig um die nötigen Formalitäten, von der Gestaltung der Traueranzeige bis hin zur Grabpflege.</p>
    <p>Sie können uns rund um die Uhr unter der Telefonnummer 03741 / 38 210 erreichen. Bei aktuellen Sterbefällen und dringenden Fragen bitten wir um Ihren Anruf.</p>
    <p>Ihr Team vom Bestattungswesen Wiesentrup</p>
  </div>
  <div class="pill pill-solid" style="left:262px;top:485px;width:222px;height:53px">LEISTUNGEN</div>
  <div class="pill pill-solid" style="left:685px;top:485px;width:222px;height:53px">KONTAKT</div>
</section>

<section class="reach">
  <h2 class="section-title" style="top:60px">EMPATHISCH · PROFESSIONELL ·24 H</h2>
  <div class="copy" style="left:200px;top:132px;width:400px">Wir sind rund um die Uhr für Sie erreichbar.<br>Sie können uns, bei aktuellen Sterbefällen jederzeit anrufen</div>
  <div class="copy" style="left:606px;top:132px;width:400px">Wir beraten Sie auch gerne persönlich bei Ihnen oder in unseren<br>Geschäftsräumen. Vereinbaren Sie hierzu gerne einen Termin.</div>
  <svg class="phone-mark" style="left:373px;top:202px;z-index:2" viewBox="0 0 40 40"><path d="M8 2l8 7-4 6c3 6 7 10 13 13l6-4 7 8-5 6C17 36 4 23 3 8z" fill="#b39b9c"/></svg>
  <div class="pill pill-light" style="left:286px;top:228px;width:222px;height:53px">SOFORTHILFE (24/7)</div>
  <div class="pill pill-light" style="left:690px;top:228px;width:222px;height:53px">KONTAKT</div>
</section>

<section class="care">
  <div class="ornament" style="top:48px" role="img" aria-label="Zierelement: gekreuzte Palmzweige"></div>
  <h2 class="section-title" style="top:117px">UNSERE LEISTUNGEN IM TRAUERFALL</h2>
  <div class="copy" style="left:185px;top:171px;width:410px">
    <p>Grundsätzlich gibt es in Deutschland zwei Bestattungsarten – die Erdbestattung und die Feuerbestattung. Die Feuerbestattung hat zahlreiche Varianten, wie zum Beispiel Urnen, –See, -Baumbestattung.</p>
    <p>Lassen Sie es uns wissen, welche Bestattungsart der Verstorbene in seiner letzten Verfügung dokumentiert hat und wir kümmern uns um eine würdevolle Bestattung.</p>
  </div>
  <div class="copy" style="left:618px;top:171px;width:400px">Falls ein Trauerfall eintritt, brauchen Sie uns nur anzurufen. Wir sprechen gerne mit Ihnen gemeinsam über alle notwendigen Formalitäten und unser Serviceangebot, natürlich auch bei Ihnen zu Hause.</div>
  <div class="pill pill-solid" style="left:616px;top:266px;width:336px;height:53px">ZU UNSEREN LEISTUNGEN</div>
</section>

<section class="gallery">
  <div class="tile tile-coffin" role="img" aria-label="Foto: Sarg mit Blumengesteck in einer Kirche"></div>
  <div class="tile tile-urn" role="img" aria-label="Foto: Urne mit Rosenkranz auf einem Holzschemel"></div>
  <div class="tile tile-mauve"></div>
  <div class="tile tile-cards" role="img" aria-label="Foto: Trauerkarten und Bilderrahmen, hell überlagert">
    <p>WIR ERSTELLEN NACH IHREN WÜNSCHEN TRAUERBRIEFE, TRAUERKARTEN, DANKSAGUNGEN UND STERBEBILDER.</p>
  </div>
  <div class="tile tile-mauve2"></div>
  <div class="tile tile-water" role="img" aria-label="Foto: Blumenkranz mit Kerze auf dem Wasser bei Sonnenuntergang"></div>
</section>

<section class="region">
  <div class="ornament" style="top:66px" role="img" aria-label="Zierelement: gekreuzte Palmzweige"></div>
  <h2 class="section-title" style="top:166px">BESTATTUNGSWESEN WIESENTRUP – IM UMLAND</h2>
  <div class="copy" style="left:330px;top:230px;width:540px">Auch im Umland von Wiesentrup sind wir für Sie da. Von Hollenried, Birkwalde, Steinhagenau, Lindholm, Rosenbrück, Erlenhausen, Talwiesen, Moosbach am Hang, Kirchwehde, Feldrade, Ahornbühl, Sonnental, Haselgrund, Dornhagen, Wiesbrunn, Grünfelde, Eichstetten-Nord, Lerchenau, Bachhofen, Tannried, Kleinmoor, Weidenrode, Holtrup, Brunnwalde, Ostersiel, Quellbach, Herzfelden, Mühlenkamp, Sandberg, Fichtenau, Rabenholz, Eichenried bis Brückental.</div>
</section>

<footer class="site-footer">
  <h3 class="foot-head" style="left:188px;top:37px">Kontaktdaten</h3>
  <div class="foot-lines" style="left:189px;top:70px">Marlene Hoffmann<br>Bestattungswesen Wiesentrup<br>Inhaberin Marlene Hoffmann<br>Lindenweg 14 | 33649 Wiesentrup</div>
  <div class="pill pill-gold" style="left:185px;top:161px;width:222px;height:54px;border:1px solid #e2c9a8">WEGKARTE</div>
  <div class="foot-lines" style="left:189px;top:224px">Telefon: 03741 38210<br>E-Mail: kontakt@bestattungen-wiesentrup.de</div>
  <h3 class="foot-head" style="left:623px;top:37px">Wir sind Mitglied</h3>
  <div class="badge" style="left:625px;width:74px"></div>
  <div class="badge" style="left:711px;width:101px"></div>
  <div class="badge" style="left:827px;width:147px"></div>
</footer>

<footer class="bottombar">
  <span>IMPRESSUM</span><span>DATENSCHUTZ</span><span>KONTAKT</span><span>BARRIEREFREIHEIT</span>
</footer>

</body>
</html>
```